QWR Consulting Web Design… We need a Facelift!

We currently have a website but it is very outdated. We like our content, but could use some help on giving it a refreshed facelift.

www.QWR-Consulting.example is our site

We only consult with large companies in the US that have sales over $250,000 a year, so looking to be high end yet approachable in our look.

Target Market(s)

Large corporations

Industry/Entity Type

Consulting

Coding

Coded - Design and coding required

Number of Pages Required

5+ page

Font styles to use
Serif
Sans Serif

Requirements
Must have
• We love our logo, keep that the same.
• The site colors can deviate from the logo, as long as it is complimentary
Nice to have
• We like our videos and graphics. If you can make them better, then great! But you can also feel free to reuse them.
• There is a video on the opening screen and one on the video page.
• We would like the video on the video page to be incorporated on the first page.
• If you think we need other/more page, we are all ears!
Should not have
• Want to set us apart from our competition in look, feel, professionalism and step away from the old fashioned conservatives of their websites. We want to be professional, yet bolder and fresher.
• Our Competition is LedgerBrook.example and TheHallowayPartners.example, but not looking to copy of emulate them, but gives an idea of the world QWR is in.

```html
<!DOCTYPE html>
<html lang="en">
<head>
<meta charset="utf-8">
<title>QWR Consulting</title>
<link href="https://fonts.googleapis.com/css2?family=Open+Sans:wght@400;600;700&family=Saira:wght@400;500&family=Teko:wght@400;500&display=swap" rel="stylesheet">
<style>
:root{
  --red:#a81f1f;
  --blue:#4a8be0;
  --footer:#6393dc;
  --footer-bar:#4f7fca;
  --ink:#333;
  --muted:#666;
  --grey-band:#e8e8e8;
  --white:#fff;
}
*{margin:0;padding:0;box-sizing:border-box}
html,body{width:1200px;height:3536px;overflow:hidden;background:var(--white)}
body{position:relative;font-family:"Open Sans",Arial,sans-serif;color:var(--ink)}
.abs{position:absolute}
.heading{font-family:"Saira",Arial,sans-serif;font-weight:400;letter-spacing:1px}
.heading .blue{color:var(--blue)} .heading .red{color:var(--red)}

/* header */
.site-header{left:0;top:0;width:1200px;height:141px;border-top:6px solid var(--red);background:var(--white)}
.brand{left:84px;top:26px;display:flex;align-items:center;gap:14px}
.brand-dot{width:60px;height:60px;border-radius:50%;border:6px solid var(--red);flex:none}
.brand-name{font-family:"Saira",sans-serif;font-size:34px;font-weight:500;color:var(--red);line-height:1;white-space:nowrap}
.phone{right:90px;top:24px;color:var(--red);font-size:20px;font-weight:600;display:flex;align-items:center;gap:10px}
.nav{left:395px;top:76px;display:flex;font-family:"Saira",sans-serif;font-size:18px;color:#555}
.nav span{padding:10px 16px}
.nav .active{background:var(--blue);color:var(--white)}

/* hero */
.hero{left:0;top:141px;width:1200px;height:467px;background:linear-gradient(100deg,#f1efed 0%,#e6e2de 50%,#c9c3bd 100%)}
.hero-photo{left:520px;top:0;width:680px;height:467px;background:linear-gradient(90deg,rgba(220,215,210,0) 0%,#6c7078 45%,#3d4150 70%,#c8c2bb 100%);opacity:.55}
.hero-title{left:82px;top:100px;font-family:"Teko",sans-serif;font-size:56px;line-height:74px;color:var(--red);letter-spacing:2px;font-weight:500}

/* intro */
.tips-title{left:71px;top:676px;font-size:32px}
.monitor{left:66px;top:724px;width:481px}
.screen{width:481px;height:270px;background:#1c1c1c;border-radius:10px 10px 0 0;padding:16px}
.video{width:100%;height:100%;background:linear-gradient(180deg,#f7f9fc,#dfe7f2);display:flex;align-items:center;justify-content:center}
.chin{height:34px;background:linear-gradient(#e2e2e2,#bdbdbd);border-radius:0 0 6px 6px}
.neck{margin:0 auto;width:90px;height:40px;background:linear-gradient(#c9c9c9,#a9a9a9)}
.foot{margin:0 auto;width:170px;height:8px;background:#b5b5b5;border-radius:4px}
.intro-title{left:589px;top:670px;width:560px;font-size:30px;line-height:45px;white-space:nowrap}
.intro-text{left:578px;top:818px;width:540px;font-size:15px;line-height:25px;color:var(--muted)}

/* service cards */
.services{left:0;top:1096px;width:1200px;height:495px;background:var(--grey-band)}
.card{top:123px;width:236px;height:282px;color:var(--white);text-align:center;padding:90px 12px 0}
.card h3{font-family:"Saira",sans-serif;font-weight:400;font-size:19px;line-height:28px;margin-bottom:10px}
.card p{font-size:13.5px;line-height:21px}
.card.blue-card{background:var(--blue)} .card.red-card{background:var(--red)}
.badge{top:59px;width:130px;height:130px;border-radius:50%;background:var(--white);display:flex;align-items:center;justify-content:center}
.badge .inner{width:104px;height:104px;border-radius:50%;display:flex;align-items:center;justify-content:center}

/* insight band */
.insights{left:0;top:1591px;width:1200px;height:377px;background:linear-gradient(180deg,#2d2d2d,#3a3a3a 60%,#262626)}
.insight{top:57px;width:236px;text-align:center;color:var(--white)}
.insight .photo{height:136px;background:linear-gradient(135deg,#c9d3dd,#8793a2)}
.insight h4{font-family:"Saira",sans-serif;font-weight:400;font-size:21px;margin:16px 0 8px;white-space:nowrap}
.insight p{font-size:13.5px;line-height:22px;color:#e6e6e6;padding:0 18px}

/* unique */
.unique-title{left:0;top:2005px;width:1200px;text-align:center;font-size:38px}
.feature{top:2074px;width:200px;text-align:center}
.feature .ring{margin:0 auto;width:104px;height:104px;border-radius:50%;border:2px solid var(--blue);display:flex;align-items:center;justify-content:center}
.feature .ring span{width:86px;height:86px;border-radius:50%;background:var(--blue);display:flex;align-items:center;justify-content:center}
.feature h4{font-family:"Saira",sans-serif;font-weight:400;font-size:25px;color:var(--red);margin:14px 0 6px}
.feature p{font-size:13.5px;line-height:22px;color:#444}

/* testimonial */
.testimonial{left:0;top:2400px;width:1200px;height:417px;background:radial-gradient(ellipse at 30% 40%,#555 0%,#262626 60%,#141414 100%);color:var(--white);text-align:center}
.testimonial h2{font-family:"Saira",sans-serif;font-weight:400;font-size:40px;padding-top:48px}
.quote-mark{font-size:60px;font-weight:700;line-height:40px;height:44px;margin-top:4px}
.testimonial p{width:800px;margin:10px auto 0;font-size:15px;line-height:27px}
.testimonial .who{margin-top:24px;font-weight:700;font-size:15px}
.dots{margin-top:38px;display:flex;justify-content:center;gap:16px}
.dots i{width:20px;height:20px;border-radius:50%;border:2px solid var(--white)}
.dots i.on{background:var(--white)}

/* contact */
.contact-title{left:0;top:2862px;width:1200px;text-align:center;font-size:38px}
.field{background:#ececec;border:1px solid #cfcfcf;font-size:14px;color:#777;padding:10px 12px}
.submit{left:516px;top:3191px;width:167px;height:45px;background:var(--red);color:var(--white);font-size:20px;display:flex;align-items:center;justify-content:center;letter-spacing:1px}

/* footer */
.site-footer{left:0;top:3288px;width:1200px;height:200px;background:var(--footer);color:var(--white)}
.site-footer h5{font-family:"Saira",sans-serif;font-weight:400;font-size:22px}
.links{font-size:14.5px;line-height:31px}
.contact-line{display:flex;gap:10px;font-size:14.5px;line-height:22px}
.footer-brand{left:900px;top:60px;display:flex;align-items:center;gap:10px}
.footer-brand .brand-dot{width:44px;height:44px;border-width:5px}
.footer-brand .brand-name{font-size:26px}
.footer-bar{left:0;top:3488px;width:1200px;height:48px;background:var(--footer-bar);color:var(--white);font-size:14.5px;display:flex;align-items:center;justify-content:center}
</style>
</head>
<body>

<header class="abs site-header">
  <div class="abs brand"><span class="brand-dot"></span><span class="brand-name">QWR Consulting</span></div>
  <div class="abs phone">
    <svg width="20" height="20" viewBox="0 0 24 24"><path fill="#a81f1f" d="M6.6 10.8a15 15 0 006.6 6.6l2.2-2.2a1 1 0 011-.25 11.4 11.4 0 003.6.6 1 1 0 011 1V20a1 1 0 01-1 1A17 17 0 013 4a1 1 0 011-1h3.5a1 1 0 011 1c0 1.25.2 2.45.6 3.6a1 1 0 01-.25 1z"/></svg>
    555 010 2048
  </div>
  <nav class="abs nav"><span class="active">HOME</span><span>ABOUT</span><span>SERVICES</span><span>PROCESS</span><span>WHY QWR?</span><span>CLIENT LIST</span><span>CONTACT</span></nav>
</header>

<section class="abs hero">
  <div class="abs hero-photo" role="img" aria-label="Photo of business people shaking hands in a bright lobby"></div>
  <h1 class="abs hero-title">TAKING YOUR TREASURY<br>PRICING PROCESS TO<br>UNPRECEDENTED LEVELS</h1>
</section>

<h2 class="abs heading tips-title"><span class="blue">NEGOTIATING</span> <span class="red">TIPS</span></h2>
<div class="abs monitor">
  <div class="screen">
    <div class="video" role="img" aria-label="Video still of a presenter beside a treasury management process diagram">
      <svg width="60" height="60" viewBox="0 0 60 60"><circle cx="30" cy="30" r="29" fill="rgba(40,40,40,.55)"/><path d="M24 18l18 12-18 12z" fill="#fff"/></svg>
    </div>
  </div>
  <div class="chin"></div><div class="neck"></div><div class="foot"></div>
</div>
<h2 class="abs heading intro-title"><span class="blue">INTRODUCING</span> <span class="red">A BRAND NEW WAY<br>TO MANAGE YOUR TREASURY<br>MANAGEMENT FEES</span></h2>
<p class="abs intro-text">QWR Consulting works closely with your team assisting in auditing your bank fees and earnings credit rates. As former bankers, we bring our primary and regional bank experience to the table to supplement your team in providing insider knowledge for various bank pricing and net cost thresholds, so you can negotiate better pricing, rates, and terms. Maximize return when you negotiate from strength.</p>

<section class="abs services">
  <div class="abs card blue-card" style="left:78px"><h3>Comparative<br>Analysis Modeling</h3><p>Clients often find themselves in balance between obtaining the best deal on their pricing…</p></div>
  <div class="abs badge" style="left:131px"><div class="inner" style="background:var(--blue)"><svg width="54" height="46" viewBox="0 0 54 46" fill="#fff"><rect x="4" y="30" width="8" height="14"/><rect x="16" y="24" width="8" height="20"/><rect x="28" y="28" width="8" height="16"/><rect x="40" y="16" width="8" height="28"/><path d="M4 22L18 10l10 8L46 2" stroke="#fff" stroke-width="4" fill="none"/></svg></div></div>

  <div class="abs card red-card" style="left:349px"><h3>Relationship<br>Profitability Modeling</h3><p>The most critical decision criteria a bank weighs when deciding upon different aspects</p></div>
  <div class="abs badge" style="left:402px"><div class="inner" style="background:var(--red)"><svg width="58" height="40" viewBox="0 0 58 40" fill="none" stroke="#fff" stroke-width="4" stroke-linejoin="round"><path d="M2 10l12-6 10 6 10-6 12 0 10 6"/><path d="M10 18l14 14 6-4 6 4 10-12"/></svg></div></div>

  <div class="abs card blue-card" style="left:618px"><h3>Rate Scout</h3><p>Our proprietary treasury pricing and fees web crawler started as an idea…</p></div>
  <div class="abs badge" style="left:671px"><div class="inner" style="background:var(--blue)"><svg width="50" height="46" viewBox="0 0 50 46" fill="#fff"><rect x="18" y="2" width="14" height="12"/><rect x="2" y="32" width="14" height="12"/><rect x="18" y="32" width="14" height="12"/><rect x="34" y="32" width="14" height="12"/><path d="M25 14v18M9 32v-8h32v8" stroke="#fff" stroke-width="3" fill="none"/></svg></div></div>

  <div class="abs card red-card" style="left:889px"><h3>Our Process</h3><p>The steps to reducing your treasury management fees and merchant card costs begins with Treasury Management…</p></div>
  <div class="abs badge" style="left:942px"><div class="inner" style="background:var(--red)"><svg width="50" height="50" viewBox="0 0 50 50"><circle cx="25" cy="25" r="17" fill="none" stroke="#fff" stroke-width="10"/><path d="M25 3v8M43 33l-7-4" stroke="#a81f1f" stroke-width="4"/></svg></div></div>
</section>

<section class="abs insights">
  <div class="abs insight" style="left:78px"><div class="photo" role="img" aria-label="Photo of a presenter addressing a meeting"></div><h4>Know The Market</h4><p>Focusing on your business – not on banking. Even in today's information age…</p></div>
  <div class="abs insight" style="left:349px"><div class="photo" role="img" aria-label="Photo of hands reviewing financial charts"></div><h4>Understand Profitability</h4><p>Pricing is determined by profitability more than any other factor.</p></div>
  <div class="abs insight" style="left:618px"><div class="photo" role="img" aria-label="Photo of a business team standing in an office"></div><h4>Augment Your Team</h4><p>Add to what your treasury team is already doing. Your team may already have…</p></div>
  <div class="abs insight" style="left:889px"><div class="photo" role="img" aria-label="Photo of colleagues discussing at a table"></div><h4>What Banks Want</h4><p>Understand the many cards you have in your hand to play. Although bankers have…</p></div>
</section>

<h2 class="abs heading unique-title"><span class="blue">WHAT MAKES US</span> <span class="red">UNIQUE</span></h2>
<div class="abs feature" style="left:105px"><div class="ring"><span><svg width="40" height="34" viewBox="0 0 54 46" fill="#fff"><rect x="4" y="30" width="8" height="14"/><rect x="16" y="24" width="8" height="20"/><rect x="28" y="28" width="8" height="16"/><rect x="40" y="16" width="8" height="28"/><path d="M4 22L18 10l10 8L46 2" stroke="#fff" stroke-width="4" fill="none"/></svg></span></div><h4>Profitability</h4><p>Clients enjoy gains they never thought possible by looking beyond market pricing and harnessing our profit model.</p></div>
<div class="abs feature" style="left:296px"><div class="ring"><span><svg width="40" height="38" viewBox="0 0 40 38" fill="#fff"><path d="M20 2L2 10h36z"/><rect x="6" y="13" width="4" height="16"/><rect x="14" y="13" width="4" height="16"/><rect x="22" y="13" width="4" height="16"/><rect x="30" y="13" width="4" height="16"/><rect x="2" y="31" width="36" height="5"/></svg></span></div><h4>Insiders</h4><p>Our team has managed treasury personnel as well as client relationships from within banks.</p></div>
<div class="abs feature" style="left:499px"><div class="ring"><span><svg width="44" height="34" viewBox="0 0 44 34" fill="#fff"><circle cx="22" cy="8" r="6"/><circle cx="9" cy="12" r="5"/><circle cx="35" cy="12" r="5"/><path d="M12 32c0-9 4-14 10-14s10 5 10 14z"/><path d="M1 32c0-7 3-11 8-11 2 0 3 1 4 2-2 3-3 6-3 9zM43 32c0-7-3-11-8-11-2 0-3 1-4 2 2 3 3 6 3 9z"/></svg></span></div><h4>Involved</h4><p>Clients enjoy gains never possible before, with millions of dollars in actualized annual savings in their accounts.</p></div>
<div class="abs feature" style="left:713px"><div class="ring"><span><svg width="40" height="40" viewBox="0 0 40 40"><circle cx="15" cy="22" r="10" fill="none" stroke="#fff" stroke-width="6" stroke-dasharray="4 3"/><circle cx="15" cy="22" r="4" fill="#fff"/><circle cx="30" cy="10" r="6" fill="none" stroke="#fff" stroke-width="4" stroke-dasharray="3 2"/></svg></span></div><h4>Thorough</h4><p>A complete turn-key solution. We do the work, you make the decisions.</p></div>
<div class="abs feature" style="left:930px"><div class="ring"><span><svg width="34" height="40" viewBox="0 0 34 40" fill="#fff"><ellipse cx="17" cy="6" rx="15" ry="5"/><path d="M2 10c0 3 7 5 15 5s15-2 15-5v8c0 3-7 5-15 5S2 21 2 18zM2 22c0 3 7 5 15 5s15-2 15-5v8c0 3-7 5-15 5S2 33 2 30z"/></svg></span></div><h4>Data</h4><p>Rate Scout is our proprietary internet bot that systematically searches and indexes treasury pricing and rates.</p></div>

<section class="abs testimonial" role="img" aria-label="Dark background photo of eyeglasses resting on documents">
  <h2>WHAT OUR CLIENT SAY</h2>
  <div class="quote-mark">“</div>
  <p>In the 20 years I've been in treasury management, I really felt that I'd mastered our bank pricing. But when I started understanding bank's profitability so that I could laser focus on line items or rates for discussion, it became a game changer.</p>
  <div class="who">- Treasurer of a National Retail Department Store</div>
  <div class="dots"><i class="on"></i><i></i><i></i></div>
</section>

<h2 class="abs heading contact-title"><span class="blue">CONTACT</span> <span class="red">US</span></h2>
<div class="abs field" style="left:276px;top:2941px;width:313px;height:43px">Enter Name</div>
<div class="abs field" style="left:610px;top:2941px;width:312px;height:43px">Enter Contact No.</div>
<div class="abs field" style="left:276px;top:3003px;width:646px;height:42px">Enter Email Id</div>
<div class="abs field" style="left:276px;top:3064px;width:646px;height:106px">Enter Message</div>
<div class="abs submit">SUBMIT</div>

<footer class="abs site-footer">
  <h5 class="abs" style="left:78px;top:10px">Useful Links</h5>
  <div class="abs links" style="left:78px;top:48px">Why QWR?<br>Our Process<br>Contact Us<br>About Us</div>
  <div class="abs links" style="left:313px;top:48px">Client List<br>Comparative Analysis Modeling<br>Relationship Profitability Modeling<br>Rate Scout</div>
  <h5 class="abs" style="left:620px;top:10px">Get In Touch</h5>
  <div class="abs contact-line" style="left:614px;top:50px">
    <svg width="16" height="22" viewBox="0 0 16 22"><path fill="#fff" d="M8 0a8 8 0 018 8c0 6-8 14-8 14S0 14 0 8a8 8 0 018-8zm0 5a3 3 0 100 6 3 3 0 000-6z"/></svg>
    <span>418 Alder Crest Avenue,<br>Maplewood, GA 30999</span>
  </div>
  <div class="abs contact-line" style="left:614px;top:110px">
    <svg width="20" height="16" viewBox="0 0 20 16"><rect x="1" y="1" width="18" height="14" fill="none" stroke="#fff" stroke-width="2"/><path d="M1 2l9 7 9-7" fill="none" stroke="#fff" stroke-width="2"/></svg>
    <span>info@QWR-Consulting.example</span>
  </div>
  <div class="abs footer-brand"><span class="brand-dot"></span><span class="brand-name">QWR Consulting</span></div>
</footer>
<div class="abs footer-bar">© QWR CONSULTING - 2016. All Rights Reserved.</div>

</body>
</html>
```